Criação de Papelaria Profissional para Beleza
A empresa queria:
" Atendemos clientes adultos masculino, feminino, adolescentes para tratamentos estéticos diversos como acne, rejuvenescimento facial, redução de medidas faciais e corporais, depilação, tratamento de celulite, estrias, medicina capilar, laser, cicatrizes, manchas, melasma, pequenos vasos, poros dilatados, limpeza de pele "

```html
<!DOCTYPE html>
<html lang="pt-BR">
<head>
<meta charset="UTF-8">
<title>Lumina Clínica Estética — Cartão</title>
<link rel="stylesheet" href="https://fonts.googleapis.com/css2?family=Marcellus&family=Nunito+Sans:wght@400;600&display=swap">
<style>
  :root {
    --backdrop: #e6e8ea;
    --card-white: #ffffff;
    --navy: #0f2a4a;
    --teal: #2bb3a6;
    --ink: #14304f;
    --ink-soft: #3d5470;
    --logo-light: #eef3f7;
  }
  * { margin: 0; padding: 0; box-sizing: border-box; }
  html, body {
    width: 1200px;
    height: 1200px;
    overflow: hidden;
    background: var(--backdrop);
  }
  .business-card {
    position: absolute;
    left: 45px;
    top: 455px;
    width: 1110px;
    height: 290px;
    background: var(--card-white);
    overflow: hidden;
    box-shadow: 0 6px 18px rgba(20, 40, 60, 0.18);
  }
  .card-shapes {
    position: absolute;
    inset: 0;
    width: 100%;
    height: 100%;
  }
  .contact-side {
    position: absolute;
    left: 62px;
    top: 52px;
    color: var(--ink);
  }
  .person-name {
    font-family: "Marcellus", serif;
    font-size: 36px;
    line-height: 1;
    letter-spacing: 0.5px;
  }
  .person-role {
    font-family: "Nunito Sans", sans-serif;
    font-size: 19px;
    color: var(--ink-soft);
    margin-top: 4px;
  }
  .contact-list {
    list-style: none;
    margin-top: 34px;
  }
  .contact-item {
    display: flex;
    align-items: center;
    gap: 16px;
    font-family: "Nunito Sans", sans-serif;
    font-size: 15px;
    line-height: 1.35;
    color: var(--ink);
  }
  .contact-item + .contact-item { margin-top: 18px; }
  .contact-icon {
    width: 34px;
    height: 34px;
    border-radius: 7px;
    background: var(--teal);
    display: flex;
    align-items: center;
    justify-content: center;
    flex-shrink: 0;
  }
  .contact-icon svg { width: 20px; height: 20px; }
  .brand-side {
    position: absolute;
    left: 640px;
    right: 0;
    top: 0;
    bottom: 0;
    display: flex;
    flex-direction: column;
    align-items: center;
    justify-content: center;
    color: var(--logo-light);
    font-family: "Marcellus", serif;
  }
  .brand-name {
    font-size: 62px;
    line-height: 1;
    letter-spacing: 3px;
  }
  .brand-tagline {
    font-size: 20px;
    letter-spacing: 7px;
    margin-top: 8px;
  }
</style>
</head>
<body>
  <div class="business-card">
    <svg class="card-shapes" viewBox="0 0 1110 290" preserveAspectRatio="none" aria-hidden="true">
      <path d="M 575 0 C 560 110, 540 210, 505 290 L 1110 290 L 1110 0 Z" fill="var(--teal)"/>
      <path d="M 600 0 C 585 110, 568 210, 548 290 L 1110 290 L 1110 0 Z" fill="var(--navy)"/>
    </svg>

    <div class="contact-side">
      <h1 class="person-name">Dra. Lívia Moraes</h1>
      <p class="person-role">Esteticista</p>
      <ul class="contact-list">
        <li class="contact-item">
          <span class="contact-icon">
            <svg viewBox="0 0 24 24" fill="none" stroke="#ffffff" stroke-width="2" stroke-linecap="round" stroke-linejoin="round">
              <path d="M22 16.9v3a2 2 0 0 1-2.2 2 19.8 19.8 0 0 1-8.6-3.1 19.5 19.5 0 0 1-6-6A19.8 19.8 0 0 1 2.1 4.2 2 2 0 0 1 4.1 2h3a2 2 0 0 1 2 1.7c.1.9.4 1.8.7 2.7a2 2 0 0 1-.5 2.1L8 9.8a16 16 0 0 0 6 6l1.3-1.3a2 2 0 0 1 2.1-.5c.9.3 1.8.6 2.7.7a2 2 0 0 1 1.7 2z"/>
            </svg>
          </span>
          <span>(11) 98431-2275</span>
        </li>
        <li class="contact-item">
          <span class="contact-icon">
            <svg viewBox="0 0 24 24" fill="#ffffff">
              <path d="M12 2a7 7 0 0 0-7 7c0 5.2 7 13 7 13s7-7.8 7-13a7 7 0 0 0-7-7zm0 9.5A2.5 2.5 0 1 1 12 6.5a2.5 2.5 0 0 1 0 5z"/>
            </svg>
          </span>
          <span>Rua das Acácias 218,<br>Vila Serena, São Paulo</span>
        </li>
      </ul>
    </div>

    <div class="brand-side">
      <div class="brand-name">LUMINA</div>
      <div class="brand-tagline">CLÍNICA ESTÉTICA</div>
    </div>
  </div>
</body>
</html>
```